Maple Rx Ventures (company name is Maple Rx Ventures LLP)

management of homestay, hospitality something similar with https://www.stayvorn.example

Target Market(s)

johor bahru market (Malaysia)

Contact Information for Business Card

Maple Ventures Rx LLP

Logo Text

eyes catching, attractive, amazing, Nice, jaw dropping for design

Coding

Coded - Design and coding required

Number of Pages Required

5+ page

Colors

Designer to choose colors to be used in the design.

Requirements
Must have
• please change the short term proposal to our company logo and change the name from stayvorn to maple RX Ventures LLP
• thanks
Nice to have
• please let me have eyes catching , jaw dropping design

```html
<!DOCTYPE html>
<html lang="en">
<head>
<meta charset="utf-8">
<title>Maple Rx Ventures</title>
<link href="https://fonts.googleapis.com/css2?family=Lato:wght@400;700;900&display=swap" rel="stylesheet">
<style>
:root{
  --brown:#4d2a0c;
  --brown-dark:#2e1604;
  --brown-light:#a4652a;
  --ink:#1f1f1f;
  --text:#444;
  --grey:#ececec;
  --grey-soft:#f3f3f3;
  --white:#fff;
  --black:#000;
}
*{box-sizing:border-box;margin:0;padding:0}
html,body{width:1200px;height:3120px;overflow:hidden}
body{font-family:'Lato',Arial,sans-serif;color:var(--text);background:var(--white);position:relative}
.abs{position:absolute}

/* header */
.site-header{left:0;top:0;width:1200px;height:108px;background:var(--white)}
.brand{left:75px;top:36px;font-size:29px;font-weight:700;color:var(--ink);letter-spacing:.3px}
.main-nav{right:75px;top:47px;display:flex;gap:42px;font-size:13px;font-weight:700;color:var(--ink)}
.main-nav .active{color:var(--brown-light)}

/* hero */
.hero{left:0;top:108px;width:1200px;height:560px;background:radial-gradient(ellipse at 30% 30%,#b8773c 0%,#6b3e1b 35%,#2a1608 75%,#140a03 100%)}
.hero-title{left:0;top:212px;width:1200px;text-align:center;color:var(--white);font-weight:900;font-size:64px;line-height:62px}
.hero-dots{left:555px;top:496px;display:flex;gap:11px}
.hero-dots span{width:13px;height:13px;border-radius:50%;background:var(--white)}
.hero-dots span.current{background:#333;border:1px solid #777}

/* about */
.about-box{left:75px;top:728px;width:422px;height:375px;background:var(--grey);padding:32px 28px}
.about-box h2{font-size:33px;font-weight:900;color:var(--ink);margin-bottom:14px}
.about-box p{font-size:14px;line-height:22px;color:#333;margin-bottom:9px}
.btn-outline{display:inline-block;margin-top:14px;border:2px solid var(--brown);color:var(--brown);font-size:14px;font-weight:700;padding:8px 22px}
.about-photo{left:497px;top:728px;width:283px;height:375px;background:linear-gradient(160deg,#3a3a3a,#111 60%,#2b2b2b)}
.start-box{left:794px;top:728px;width:332px;height:375px;background:var(--black);color:var(--white);padding:30px 20px}
.start-box h2{font-size:32px;font-weight:900;margin-bottom:12px}
.start-box .lead{font-size:13.5px;line-height:20px;margin-bottom:20px}
.steps{list-style:none}
.steps li{display:flex;align-items:center;gap:16px;font-size:13.5px;line-height:19px;margin-bottom:17px}
.steps b{flex:none;width:32px;height:32px;border-radius:50%;background:var(--brown);display:flex;align-items:center;justify-content:center;font-size:15px}

/* services */
.services{left:0;top:1165px;width:1200px;height:537px;background:linear-gradient(120deg,#3c1e05 0%,#5a2f0c 30%,#b06a2a 42%,#4a2508 62%,#2a1402 100%)}
.section-title{width:1200px;left:0;text-align:center;font-weight:900;font-size:32px}
.services .section-title{top:45px;color:var(--white)}
.service-card{top:111px;width:331px;height:370px;background:var(--white);text-align:center}
.service-card .photo{height:187px}
.service-card h3{margin:21px 14px 8px;font-size:16.5px;font-weight:900;color:var(--brown);line-height:22px}
.service-card p{font-size:13.5px;line-height:21px;color:#222;padding:0 22px}

/* pricing */
.pricing-title{top:1740px;color:var(--brown)}
.package{top:1858px;width:512px;height:350px;border:1px solid #ccc;background:var(--white)}
.package-tab{top:1822px;width:403px;height:73px;background:var(--brown);color:var(--white);font-weight:900;font-size:21px;display:flex;align-items:center;justify-content:center}
.features{list-style:none;position:absolute;top:60px;font-size:15px;color:#333}
.features li{display:flex;gap:16px;line-height:20px;margin-bottom:12px}
.features svg{flex:none;margin-top:2px}
.price{position:absolute;left:26px;top:278px;font-size:22px;font-weight:700;color:#333}
.terms{position:absolute;left:200px;top:285px;font-size:13px;color:var(--brown-light)}
.arrow{top:2015px}

/* blog */
.blog{left:0;top:2260px;width:1200px;height:495px;background:var(--grey-soft)}
.blog .section-title{top:42px;color:var(--brown)}
.post{top:103px;width:331px}
.post .photo{height:187px}
.post h3{margin-top:13px;font-size:22px;font-weight:900;color:var(--brown)}
.post p{margin-top:6px;font-size:14px;line-height:21px;color:#333}
.post .more{display:block;margin-top:14px;font-size:13px;font-weight:900;color:var(--brown)}

/* subscribe */
.subscribe{left:75px;top:2793px;width:700px}
.subscribe h2{font-size:24px;font-weight:900;color:var(--ink)}
.subscribe p{margin-top:14px;font-size:16px;color:#333}
.subscribe-form{margin-top:28px;display:flex;width:692px;height:48px;border:2px solid #999}
.subscribe-form span{flex:1;padding:14px;font-size:14px;color:#333}
.subscribe-form b{width:116px;background:var(--brown);color:var(--white);display:flex;align-items:center;justify-content:center;font-size:16px}
.quick-contact{left:794px;top:2800px;width:332px;height:130px;background:var(--black);color:var(--white);padding:14px 20px}
.quick-contact h2{font-size:23px;font-weight:900}
.quick-contact p{margin-top:5px;font-size:13.5px;line-height:20px}

/* footer */
.site-footer{left:0;top:2975px;width:1200px;height:145px;background:var(--black);color:var(--white);text-align:center}
.site-footer small{display:block;margin-top:44px;font-size:13px}
.social{display:flex;justify-content:center;gap:22px;margin-top:22px}
.social span{width:22px;height:22px;border-radius:50%;background:var(--white)}
</style>
</head>
<body>

<header class="site-header abs">
  <div class="brand abs">MAPLE RX VENTURES</div>
  <nav class="main-nav abs">
    <span class="active">HOME</span><span>ABOUT US</span><span>SERVICES</span><span>PACKAGES</span><span>BLOG</span><span>CONTACT</span>
  </nav>
</header>

<section class="hero abs" role="img" aria-label="Hotel bedroom with rolled towels on a made bed and bedside lamps">
  <h1 class="hero-title abs">WELCOME TO<br>MAPLE RX VENTURES</h1>
  <div class="hero-dots abs"><span class="current"></span><span></span><span></span><span></span></div>
</section>

<section class="about-box abs">
  <h2>ABOUT US</h2>
  <p>We are a short-term rental management and provides hospitality services to help property owners maximise their rental income.</p>
  <p>Our goal is to help you reap the most from your rental income without you having to do any of the hard work such as handle all the particular renting problems on Nestora, Roomvista, cleaning and dealing with tenants and guests.</p>
  <span class="btn-outline">READ MORE</span>
</section>
<div class="about-photo abs" role="img" aria-label="Butler in a tuxedo holding a tray with a small model house"></div>
<section class="start-box abs">
  <h2>HOW TO START?</h2>
  <p class="lead">The following steps are required in order to get your place ready to start.</p>
  <ol class="steps">
    <li><b>1</b>Getting the required items</li>
    <li><b>2</b>Renovation &amp; Furnishing</li>
    <li><b>3</b>Sign a management agreement</li>
    <li><b>4</b>Handover Keys &amp; Access cards, and relevant information</li>
  </ol>
</section>

<section class="services abs">
  <h2 class="section-title abs">OUR HASSLE-FREE FULL HOSPITALITY SERVICE</h2>
  <article class="service-card abs" style="left:75px">
    <div class="photo" role="img" aria-label="Two people shaking hands outdoors" style="background:linear-gradient(135deg,#8a6a4e,#c9b29a 50%,#5b4a3c)"></div>
    <h3>ANSWERING ENQUIRIES,<br>CHECK-INS / OUTS</h3>
    <p>We will answer all guest's enquiries, meet them to handover key and verification check. We also provide 24hr on-call support.</p>
  </article>
  <article class="service-card abs" style="left:434px">
    <div class="photo" role="img" aria-label="Person mopping a kitchen floor" style="background:linear-gradient(180deg,#e8e8e6,#d7d4cf 60%,#a17b52)"></div>
    <h3>CLEANING, LAUNDRY AND<br>MAINTENANCE</h3>
    <p>We get the professional cleaning team to clean up the place after the guest checked-out every time.</p>
  </article>
  <article class="service-card abs" style="left:795px">
    <div class="photo" role="img" aria-label="Person working on a laptop showing charts" style="background:linear-gradient(135deg,#3a3530,#9c8a75 55%,#5c4b3b)"></div>
    <h3>MARKETING<br>&amp; OPTIMIZATION</h3>
    <p>We take professional photos and write persuasive copywriting to optimize your listing in order to get more booking.</p>
  </article>
</section>

<h2 class="section-title pricing-title abs">PRICING PACKAGES</h2>
<svg class="arrow abs" style="left:42px" width="18" height="30" viewBox="0 0 18 30"><path d="M15 3 3 15l12 12" fill="none" stroke="#777" stroke-width="4"/></svg>
<svg class="arrow abs" style="left:1140px" width="18" height="30" viewBox="0 0 18 30"><path d="M3 3l12 12L3 27" fill="none" stroke="#777" stroke-width="4"/></svg>

<section class="package abs" style="left:75px">
  <ul class="features" style="left:26px">
    <li><svg width="16" height="16" viewBox="0 0 16 16"><circle cx="8" cy="8" r="8" fill="#111"/><path d="M6 4.5 9.5 8 6 11.5" fill="none" stroke="#fff" stroke-width="2"/></svg>Full Height Day &amp; Night curtain</li>
    <li><svg width="16" height="16" viewBox="0 0 16 16"><circle cx="8" cy="8" r="8" fill="#111"/><path d="M6 4.5 9.5 8 6 11.5" fill="none" stroke="#fff" stroke-width="2"/></svg>Main Entrance Door Grill</li>
    <li><svg width="16" height="16" viewBox="0 0 16 16"><circle cx="8" cy="8" r="8" fill="#111"/><path d="M6 4.5 9.5 8 6 11.5" fill="none" stroke="#fff" stroke-width="2"/></svg>Supply &amp; Install LED Surface Light</li>
    <li><svg width="16" height="16" viewBox="0 0 16 16"><circle cx="8" cy="8" r="8" fill="#111"/><path d="M6 4.5 9.5 8 6 11.5" fill="none" stroke="#fff" stroke-width="2"/></svg>Supply &amp; Install Down Light</li>
    <li><svg width="16" height="16" viewBox="0 0 16 16"><circle cx="8" cy="8" r="8" fill="#111"/><path d="M6 4.5 9.5 8 6 11.5" fill="none" stroke="#fff" stroke-width="2"/></svg>Supply &amp; Install Ceiling Fan</li>
    <li><svg width="16" height="16" viewBox="0 0 16 16"><circle cx="8" cy="8" r="8" fill="#111"/><path d="M6 4.5 9.5 8 6 11.5" fill="none" stroke="#fff" stroke-width="2"/></svg>Retractive Hanging Rack</li>
  </ul>
  <div class="price">RM7,950.00</div>
  <div class="terms">(*Terms And Conditions Apply)</div>
</section>
<div class="package-tab abs" style="left:130px">ECONOMIC PACKAGE</div>

<section class="package abs" style="left:615px">
  <ul class="features" style="left:26px">
    <li><svg width="16" height="16" viewBox="0 0 16 16"><circle cx="8" cy="8" r="8" fill="#111"/><path d="M6 4.5 9.5 8 6 11.5" fill="none" stroke="#fff" stroke-width="2"/></svg>Sofa bed</li>
    <li><svg width="16" height="16" viewBox="0 0 16 16"><circle cx="8" cy="8" r="8" fill="#111"/><path d="M6 4.5 9.5 8 6 11.5" fill="none" stroke="#fff" stroke-width="2"/></svg>Coffee table</li>
    <li><svg width="16" height="16" viewBox="0 0 16 16"><circle cx="8" cy="8" r="8" fill="#111"/><path d="M6 4.5 9.5 8 6 11.5" fill="none" stroke="#fff" stroke-width="2"/></svg>Dining table set with 6-seaters</li>
    <li><svg width="16" height="16" viewBox="0 0 16 16"><circle cx="8" cy="8" r="8" fill="#111"/><path d="M6 4.5 9.5 8 6 11.5" fill="none" stroke="#fff" stroke-width="2"/></svg>Queen mattress with divan<br>&amp; headboard</li>
    <li><svg width="16" height="16" viewBox="0 0 16 16"><circle cx="8" cy="8" r="8" fill="#111"/><path d="M6 4.5 9.5 8 6 11.5" fill="none" stroke="#fff" stroke-width="2"/></svg>Microfiber pillows</li>
  </ul>
  <ul class="features" style="left:320px">
    <li><svg width="16" height="16" viewBox="0 0 16 16"><circle cx="8" cy="8" r="8" fill="#111"/><path d="M6 4.5 9.5 8 6 11.5" fill="none" stroke="#fff" stroke-width="2"/></svg>Carpet rug</li>
    <li><svg width="16" height="16" viewBox="0 0 16 16"><circle cx="8" cy="8" r="8" fill="#111"/><path d="M6 4.5 9.5 8 6 11.5" fill="none" stroke="#fff" stroke-width="2"/></svg>Ironing board</li>
    <li><svg width="16" height="16" viewBox="0 0 16 16"><circle cx="8" cy="8" r="8" fill="#111"/><path d="M6 4.5 9.5 8 6 11.5" fill="none" stroke="#fff" stroke-width="2"/></svg>Bedside tables</li>
    <li><svg width="16" height="16" viewBox="0 0 16 16"><circle cx="8" cy="8" r="8" fill="#111"/><path d="M6 4.5 9.5 8 6 11.5" fill="none" stroke="#fff" stroke-width="2"/></svg>Table lamp</li>
    <li><svg width="16" height="16" viewBox="0 0 16 16"><circle cx="8" cy="8" r="8" fill="#111"/><path d="M6 4.5 9.5 8 6 11.5" fill="none" stroke="#fff" stroke-width="2"/></svg>Clothes hanger at<br>common room</li>
  </ul>
  <div class="price">RM9,900.00</div>
</section>
<div class="package-tab abs" style="left:668px">FURNITURE PACKAGE</div>

<section class="blog abs">
  <h2 class="section-title abs">BLOG POSTS</h2>
  <article class="post abs" style="left:75px">
    <div class="photo" role="img" aria-label="Modern kitchen with bar stools" style="background:linear-gradient(180deg,#e4e2df,#8d8a86 55%,#3b2c22)"></div>
    <h3>Lorem ipsum dolor sit amet..</h3>
    <p>Cras orci ipsum, accumsan id enim et, dapibus tristique massa commodo mi eu nibh scelerisque commodo...</p>
    <span class="more">READ MORE</span>
  </article>
  <article class="post abs" style="left:434px">
    <div class="photo" role="img" aria-label="Waiter holding a tray with a small model house" style="background:linear-gradient(180deg,#2a2a2a,#111 70%,#3a3a3a)"></div>
    <h3>Lorem ipsum dolor sit amet..</h3>
    <p>Cras orci ipsum, accumsan id enim et, dapibus tristique massa commodo mi eu nibh scelerisque commodo...</p>
    <span class="more">READ MORE</span>
  </article>
  <article class="post abs" style="left:795px">
    <div class="photo" role="img" aria-label="Living room with grey sofa and lamps" style="background:linear-gradient(135deg,#5a5048,#bdb3a6 50%,#3e3832)"></div>
    <h3>Lorem ipsum dolor sit amet..</h3>
    <p>Cras orci ipsum, accumsan id enim et, dapibus tristique massa commodo mi eu nibh scelerisque commodo...</p>
    <span class="more">READ MORE</span>
  </article>
</section>

<section class="subscribe abs">
  <h2>EMAIL SUBSCRIBE</h2>
  <p>Nunc placerat sodales nulla, blandit vehicula mi pellentesque ac...</p>
  <div class="subscribe-form"><span>Enter Email Address</span><b>SIGN UP</b></div>
</section>
<section class="quick-contact abs">
  <h2>QUICK CONTACT</h2>
  <p>L12-07 Cedar Residence, Jalan Meranti,<br>Taman Seri Alam, 81750<br>Johor Bahru.</p>
</section>

<footer class="site-footer abs">
  <small>Copyright © 2018. Maple Rx Ventures LLP All Right Reserved</small>
  <div class="social"><span></span><span></span><span></span><span></span><span></span></div>
</footer>

</body>
</html>
```